Business Card Design

My company is a health food catering and delivery business. Our colours are a bright turquiose green/blue, black, white and natural brown based beige. I would like the front of my card (working from the outside in; with a turquoise green boarder -quite thick, with a thin black line separating the turquoise boarder from the beige inside the remaining space of the front of the card with my logo in the centre. This should be all that appears on the front.

On the back I would like all the information displayed above on the beige coloured card, with the blurb in the bright turquoise and my contact information in black please. I would like my business name central - Harvest Lantern Kitchen and immediately below with a right alignment - ...Dine with Delight
Below this should follow all that I have displayed above with a left alignment.

Target Market(s)

Cafes, restaurants, individuals, buying agents & super markets

Industry/Entity Type

Catering

Contact Information for Business Card

BACK OF BUSINESS CARD:
Harvest Lantern Kitchen
...Dine with Delight
Deliciously healthy foods - free from gluten, lactose, cane sugar, trans-fat, GMO corn, soy & rice, no artificial flavours, colours or preservatives.
Prepared fresh from locally sourced ingredients, delivered to your door! For individuals, families, corporate, cafes, restaurants & event catering for Toowoomba & surrounds!

PH: 0491 382 907 // orders@harvestlanternkitchen.example
www.harvestlanternkitchen.example
www.social.example/harvestlanternkitchen

Requirements
Must have
• Please supply a modern, easy to read text that will blend nicely with my logo text.
Nice to have
• I really want my business cards to stand out as these will be the template for brochures, menus and website designers to draw inspiration from!
Should not have
• Please do not use Arial, Tahoma or Times Roman text.

```html
<!DOCTYPE html>
<html lang="en">
<head>
<meta charset="utf-8">
<title>Harvest Lantern Kitchen – Business Card</title>
<link rel="stylesheet" href="https://fonts.googleapis.com/css2?family=Anton&family=Oswald:wght@400;500;600&family=Roboto:wght@400;500&display=swap">
<style>
  :root {
    --stage: #2a2530;
    --turquoise: #14b8b2;
    --turquoise-text: #0e9f9a;
    --black: #111111;
    --beige: #e9dcc4;
    --beige-deep: #d9c6a5;
    --brown: #8a6c4a;
  }
  * { box-sizing: border-box; margin: 0; padding: 0; }
  html, body {
    width: 1200px; height: 800px; overflow: hidden;
    background: var(--stage);
  }
  .stage {
    position: relative; width: 1200px; height: 800px;
    display: flex; align-items: center; justify-content: center; gap: 56px;
  }
  .card {
    position: relative; width: 520px; height: 297px;
    border-radius: 4px; overflow: hidden;
    box-shadow: 0 14px 34px rgba(0,0,0,.45);
  }

  /* Front: turquoise border, thin black line, beige field */
  .card-front {
    background: var(--turquoise);
    padding: 20px;
  }
  .front-field {
    width: 100%; height: 100%;
    border: 2px solid var(--black);
    background: var(--beige);
    display: flex; flex-direction: column; align-items: center; justify-content: center;
  }
  .chef-illustration {
    width: 200px; height: 120px; border-radius: 6px;
    background: linear-gradient(160deg, var(--beige-deep), rgba(138,108,74,.35));
  }
  .brand-name {
    margin-top: 10px;
    font-family: "Oswald", sans-serif; font-weight: 500;
    font-size: 28px; line-height: 1.1; color: var(--black); letter-spacing: .5px;
  }

  /* Back: beige card, turquoise blurb, black contacts */
  .card-back {
    background: var(--beige);
    display: flex; flex-direction: column;
    padding: 20px 26px 16px;
  }
  .back-heading {
    font-family: "Anton", sans-serif; font-weight: 400; font-size: 30px; line-height: 1;
    color: var(--black); letter-spacing: 1px; text-align: center;
    text-transform: uppercase;
  }
  .back-tagline {
    font-family: "Anton", sans-serif; font-size: 15px; line-height: 1.2;
    color: var(--black); letter-spacing: .6px; text-align: right; margin-top: 4px;
    text-transform: uppercase;
  }
  .back-blurb {
    margin-top: 10px;
    font-family: "Oswald", sans-serif; font-weight: 500; font-size: 10.5px;
    line-height: 1.45; color: var(--turquoise-text); letter-spacing: .4px; text-align: left;
    text-transform: uppercase;
  }
  .contact-band {
    margin-top: auto;
    border-top: 1px solid var(--black);
    padding-top: 10px;
    display: flex; justify-content: space-between;
    font-family: "Roboto", sans-serif; font-weight: 400; font-size: 10px;
    color: var(--black);
  }
  .contact-column { display: flex; flex-direction: column; gap: 7px; }
  .contact-item { display: flex; align-items: center; gap: 7px; white-space: nowrap; }
  .contact-icon { width: 11px; height: 11px; flex: none; }
  .contact-icon * { fill: none; stroke: var(--black); stroke-width: 1.3; }
  .contact-icon .solid { fill: var(--black); stroke: none; }
</style>
</head>
<body>
<main class="stage">
  <section class="card card-front" aria-label="Card front">
    <div class="front-field">
      <div class="chef-illustration" role="img" aria-label="Line illustration of a chef holding a whisk and a frying pan"></div>
      <p class="brand-name">Harvest Lantern Kitchen</p>
    </div>
  </section>

  <section class="card card-back" aria-label="Card back">
    <h1 class="back-heading">Harvest Lantern Kitchen</h1>
    <p class="back-tagline">...Dine with Delight</p>
    <p class="back-blurb">
      Deliciously healthy foods – free from gluten, lactose, cane sugar, trans-fat,
      GMO corn, soy &amp; rice, no artificial flavours, colours or preservatives.
      Prepared fresh from locally sourced ingredients, delivered to your door!
      For individuals, families, corporate, cafes, restaurants &amp; event catering
      for Toowoomba &amp; surrounds!
    </p>
    <div class="contact-band">
      <div class="contact-column">
        <p class="contact-item">
          <svg class="contact-icon" viewBox="0 0 12 12" aria-hidden="true"><path class="solid" d="M2.3 1l2 .2.8 2.4-1.2 1a6.5 6.5 0 0 0 3.4 3.4l1-1.2 2.4.8.2 2c-.3.6-1 .9-1.7.9C5 10.3 1.7 7 1.4 2.7c0-.7.3-1.4.9-1.7z"/></svg>
          0491 382 907
        </p>
        <p class="contact-item">
          <svg class="contact-icon" viewBox="0 0 12 12" aria-hidden="true"><rect x="1" y="2.5" width="10" height="7"/><path d="M1 2.5l5 4 5-4"/></svg>
          orders@harvestlanternkitchen.example
        </p>
      </div>
      <div class="contact-column">
        <p class="contact-item">
          <svg class="contact-icon" viewBox="0 0 12 12" aria-hidden="true"><circle cx="6" cy="6" r="4.8"/><path d="M1.2 6h9.6M6 1.2c-2.4 2.6-2.4 7 0 9.6M6 1.2c2.4 2.6 2.4 7 0 9.6"/></svg>
          www.harvestlanternkitchen.example
        </p>
        <p class="contact-item">
          <svg class="contact-icon" viewBox="0 0 12 12" aria-hidden="true"><circle class="solid" cx="6" cy="6" r="5"/></svg>
          www.social.example/harvestlanternkitchen
        </p>
      </div>
    </div>
  </section>
</main>
</body>
</html>
```